Harlow Stonefield Civil Construction website design

We want a Bold website to promote our Heavy Civil Construction company, We would like an organic / tangible feel to the site. The pictures will be over saturated so they pop. We need to be able to easliy upload new projects and pictures on a regular basis.
Home page will have a full screen width image, "home page image" with silhouette and logo. It will also have about us area and picture
Page 2 will be Project Gallery with pictures in project folders
Page 3 will be an employment application form and submission
Page 4 will be Contact Us
Target Market(s)
Construction indusrty
Industry/Entity Type
Contractor
Coding
Coded - Design and coding required
Number of Pages Required
4 page
Font styles to use
Other font styles liked:
- Hypatia Sans Pro Light
Look and feel

```html
<!DOCTYPE html>
<html lang="en">
<head>
<meta charset="utf-8">
<title>Harlow Stonefield Civil Construction</title>
<link rel="stylesheet" href="https://fonts.googleapis.com/css2?family=Jost:wght@300;400;500;600&family=Open+Sans:wght@700&display=swap">
<style>
:root{
  --blue:#3a55a8;
  --blue-dark:#2f4796;
  --ink:#111111;
  --text:#2a2a2a;
  --paper:#ffffff;
  --mist:#f4f4f5;
  --night:#171717;
  --white:#ffffff;
}
*{box-sizing:border-box;margin:0;padding:0}
html,body{width:1200px;height:2862px;overflow:hidden}
body{position:relative;background:var(--paper);font-family:"Jost",sans-serif;font-weight:300;color:var(--text)}
.abs{position:absolute}

/* header */
.brand{position:absolute;display:flex;align-items:center;gap:10px;color:var(--white)}
.brand-square{width:44px;height:44px;border:3px solid currentColor}
.brand-name{font-family:"Jost",sans-serif;font-weight:500;line-height:1.05;text-transform:uppercase}
.brand-name span{display:block}
.brand-name .line-1{font-size:22px}
.brand-name .line-2{font-size:12px;letter-spacing:4.5px}
.site-header .brand{left:164px;top:30px}
.main-nav{position:absolute;top:47px;left:0;width:1200px;height:20px;font-size:14px;color:var(--white)}
.main-nav a{position:absolute;color:inherit;text-decoration:none}
.search-icon{position:absolute;left:1021px;top:49px}

/* hero */
.hero{position:absolute;left:0;top:0;width:1200px;height:660px;clip-path:polygon(0 0,1200px 0,1200px 603px,600px 657px,0 603px);
  background:linear-gradient(180deg,#6f93c4 0%,#8fa9cc 28%,#b39a4a 50%,#7b6a3e 72%,#4a3d2c 100%)}
.hero-shade{position:absolute;inset:0;background:rgba(20,30,70,.28)}
.hero-rule{position:absolute;left:0;top:0}
.hero-title{position:absolute;top:258px;width:1200px;text-align:center;font-family:"Open Sans",sans-serif;font-weight:700;font-size:68px;letter-spacing:-.5px;color:var(--white)}
.hero-lead{position:absolute;top:340px;left:280px;width:640px;text-align:center;font-size:14px;line-height:29px;color:var(--white)}
.btn{position:absolute;display:flex;align-items:center;justify-content:center;background:var(--blue);color:var(--white);border-radius:5px;font-size:13px;text-decoration:none}
.btn-hero{left:534px;top:418px;width:133px;height:50px;font-size:14px;border:1px solid rgba(255,255,255,.7)}
.slider-dots{position:absolute;top:544px;left:567px;display:flex;gap:7px}
.slider-dots i{display:block;width:16px;height:16px;border:1.5px solid var(--white);border-radius:50%}
.slider-dots i.on{background:var(--white)}

/* about */
.about-photo{position:absolute;left:164px;top:709px;width:367px;height:380px;
  background:linear-gradient(180deg,#5f8fd0 0%,#9ec0e6 30%,#c9a83c 55%,#6b5a3e 80%,#3e3427 100%)}
.section-title{font-family:"Jost",sans-serif;font-weight:600;color:var(--ink);font-size:40px}
.about-title{position:absolute;left:587px;top:730px}
.about-rule{position:absolute;left:587px;top:786px;width:111px;height:2px;background:var(--blue)}
.about-copy{position:absolute;left:587px;top:816px;width:464px;font-size:11.3px;line-height:25px}
.btn-about{left:588px;top:993px;width:119px;height:40px;font-size:12px}

/* projects */
.projects-band{position:absolute;left:0;top:1128px;width:1200px;height:956px;background:var(--blue);
  clip-path:polygon(0 0,600px 59px,1200px 0,1200px 881px,600px 955px,0 881px)}
.projects-title{position:absolute;top:1244px;width:1200px;text-align:center;color:var(--white)}
.divider{position:absolute;left:503px;width:195px;height:40px}
.divider .line{position:absolute;top:19px;width:69px;height:1px;background:currentColor}
.divider .line.l{left:0}.divider .line.r{right:0}
.divider .mark{position:absolute;left:82px;top:4px;width:32px;height:32px;border:3px solid currentColor}
.filter-tabs{position:absolute;left:146px;top:1399px;width:357px;height:42px;display:flex;border:1px solid var(--white);border-radius:5px;overflow:hidden;color:var(--white);font-size:11.5px}
.filter-tabs span{flex:1;display:flex;align-items:center;justify-content:center;border-left:1px solid rgba(255,255,255,.7)}
.filter-tabs span:first-child{border-left:0;background:var(--white);color:var(--ink);flex:1.2}
.pager{position:absolute;top:1403px;width:34px;height:34px;background:var(--white);border-radius:5px;display:flex;align-items:center;justify-content:center}
.project-card{position:absolute;width:211px}
.project-photo{width:211px;height:179px;border-radius:16px;overflow:hidden;position:relative}
.project-name{margin:14px 0 0 28px;font-weight:600;font-size:14px;color:var(--white)}
.project-hover{position:absolute;inset:0;background:rgba(20,20,20,.55);padding:50px 20px 0 20px;color:var(--white);font-size:11px;line-height:22px}
.project-hover .mini-btn{display:inline-block;margin-top:10px;background:var(--white);color:var(--blue);font-size:9px;padding:2px 15px;border-radius:4px}

/* employment */
.employment{position:absolute;left:0;top:2009px;width:1200px;height:508px;background:var(--mist)}
.employment-title{position:absolute;top:2134px;width:1200px;text-align:center}
.employment-copy{position:absolute;left:222px;top:2272px;width:760px;text-align:center;font-size:11.6px;line-height:29px}
.btn-employment{left:534px;top:2411px;width:133px;height:41px;font-size:12px}

/* footer */
.site-footer{position:absolute;left:0;top:2517px;width:1200px;height:309px;background:var(--night);color:var(--white)}
.site-footer .brand{left:457px;top:72px}
.footer-nav{position:absolute;top:170px;left:0;width:1200px;font-size:14px}
.footer-nav a{position:absolute;color:var(--white);text-decoration:none}
.social{position:absolute;top:221px;width:40px;height:40px;border:2px solid var(--white);border-radius:50%;background:var(--blue)}
.legal-bar{position:absolute;left:0;top:2826px;width:1200px;height:36px;background:var(--blue);color:var(--white);font-size:11px}
.legal-bar .copy{position:absolute;left:170px;top:11px}
.legal-bar .links{position:absolute;right:189px;top:11px}
</style>
</head>
<body>

<section class="hero" role="img" aria-label="Photo of a yellow excavator digging on a site under a blue sky with a crew member">
  <div class="hero-shade"></div>
</section>
<svg class="hero-rule" width="1200" height="662" aria-hidden="true"><polyline points="0,605 600,659 1200,605" fill="none" stroke="#d9d9d9" stroke-width="3"/></svg>

<header class="site-header">
  <div class="brand"><i class="brand-square"></i><div class="brand-name"><span class="line-1">Harlow Stonefield</span><span class="line-2">Civil Construction</span></div></div>
  <nav class="main-nav">
    <a style="left:554px">Home</a>
    <a style="left:634px">About Us</a>
    <a style="left:732px">Gallery</a>
    <a style="left:817px">Employment</a>
    <a style="left:931px">Contact Us</a>
  </nav>
  <svg class="search-icon" width="14" height="14" viewBox="0 0 14 14" aria-label="Search"><circle cx="6" cy="6" r="4.3" fill="none" stroke="#fff" stroke-width="2"/><line x1="9" y1="9" x2="13" y2="13" stroke="#fff" stroke-width="2.2"/></svg>
</header>

<h1 class="hero-title">HARLOW STONEFIELD</h1>
<p class="hero-lead">Lorem Ipsum is simply dummy text of the printing and typesetting industry. Lorem Ipsum has been the industry's standard dummy text ever since the 1500s, when an unknown printer</p>
<a class="btn btn-hero">Learn More</a>
<div class="slider-dots"><i></i><i class="on"></i><i></i></div>

<section class="about">
  <div class="about-photo" role="img" aria-label="Excavator and crew on a work site under a blue sky"></div>
  <h2 class="section-title about-title">About Us</h2>
  <div class="about-rule"></div>
  <p class="about-copy">Lorem Ipsum is simply dummy text of the printing and typesetting industry. Lorem Ipsum has been the industry's standard dummy text ever since the 1500s, when an unknown printer took a galley of type and scrambled it to make a type specimen book. It has survived not only five centuries, but also the leap into electronic typesetting, remaining essentially unchanged. It was popularised in the 1960s with the release of Letraset sheets containing Lorem Ipsum passages, and more recently with desktop publishing software like Aldus PageMaker including versions of Lorem Ipsum.</p>
  <a class="btn btn-about">Learn More</a>
</section>

<section class="projects">
  <div class="projects-band"></div>
  <h2 class="section-title projects-title">Our Latest Project</h2>
  <div class="divider" style="top:1310px;color:#fff"><i class="line l"></i><i class="mark"></i><i class="line r"></i></div>
  <div class="filter-tabs"><span>All Project</span><span>Lorem</span><span>Lorem</span><span>Lorem</span><span>Lorem</span></div>
  <div class="pager" style="left:938px"><svg width="10" height="12"><polyline points="7,1 2,6 7,11" fill="none" stroke="#3a55a8" stroke-width="2"/></svg></div>
  <div class="pager" style="left:987px"><svg width="10" height="12"><polyline points="3,1 8,6 3,11" fill="none" stroke="#3a55a8" stroke-width="2"/></svg></div>

  <div class="project-card" style="left:142px;top:1497px"><div class="project-photo" role="img" aria-label="Dump truck unloading gravel beside workers" style="background:linear-gradient(160deg,#5d7148,#8d8674 55%,#bcb7ae)"></div><p class="project-name">Project 1</p></div>
  <div class="project-card" style="left:378px;top:1497px"><div class="project-photo" role="img" aria-label="Cleared land with trees and machinery" style="background:linear-gradient(170deg,#6e7379,#4c4a3b 60%,#2f2c22)"><div class="project-hover">Lorem Ipsum is simply dummy text of the printing and typesetting industry.<br><span class="mini-btn">Learn More</span></div></div><p class="project-name">Project 1</p></div>
  <div class="project-card" style="left:612px;top:1497px"><div class="project-photo" role="img" aria-label="Aerial view of a graded site beside a building" style="background:linear-gradient(160deg,#8b9487,#a89f82 50%,#4f6040)"></div><p class="project-name">Project 1</p></div>
  <div class="project-card" style="left:847px;top:1497px"><div class="project-photo" role="img" aria-label="Yellow bulldozer working in sand" style="background:linear-gradient(160deg,#8a9a74,#cfc9bd 50%,#e2ddd4)"></div><p class="project-name">Project 1</p></div>

  <div class="project-card" style="left:142px;top:1737px"><div class="project-photo" role="img" aria-label="Worker in a trench with a yellow trench box and pipe" style="background:linear-gradient(160deg,#8e7a61,#b59a4c 55%,#7f8a70)"></div><p class="project-name">Project 1</p></div>
  <div class="project-card" style="left:378px;top:1737px"><div class="project-photo" role="img" aria-label="Crew working beside a truck at a trench" style="background:linear-gradient(160deg,#a9b7c6,#5e5a50 50%,#3b3830)"></div><p class="project-name">Project 1</p></div>
  <div class="project-card" style="left:612px;top:1737px"><div class="project-photo" role="img" aria-label="Drainage channel lined with concrete blocks" style="background:linear-gradient(170deg,#5f7a3f,#2f3b26 55%,#cfcabd)"></div><p class="project-name">Project 1</p></div>
  <div class="project-card" style="left:847px;top:1737px"><div class="project-photo" role="img" aria-label="Long reach excavator at a pond edge" style="background:linear-gradient(170deg,#4c7ad0,#7b9a5a 45%,#767469)"></div><p class="project-name">Project 1</p></div>
</section>

<section class="employment">
</section>
<h2 class="section-title employment-title">Employment</h2>
<div class="divider" style="top:2206px;color:#111"><i class="line l"></i><i class="mark"></i><i class="line r"></i></div>
<p class="employment-copy">Lorem Ipsum is simply dummy text of the printing and typesetting industry. Lorem Ipsum has been the industry's standard dummy text ever since the 1500s, when an unknown printer took a galley of type and scrambled it to make a type specimen book. It has survived not only five centuries, but also the leap into electronic typesetting, remaining essentially unchanged. It was popularised in the 1960s with the release of Letraset sheets containing Lorem Ipsum passages, and more recently with desktop publishing software like Aldus PageMaker including versions of Lorem Ipsum.</p>
<a class="btn btn-employment">Emplyment Form</a>

<footer class="site-footer">
  <div class="brand"><i class="brand-square"></i><div class="brand-name"><span class="line-1">Harlow Stonefield</span><span class="line-2">Civil Construction</span></div></div>
  <nav class="footer-nav">
    <a style="left:362px">Home</a>
    <a style="left:451px">About Us</a>
    <a style="left:559px">Gallery</a>
    <a style="left:653px">Employment</a>
    <a style="left:777px">Contact Us</a>
  </nav>
  <a class="social" style="left:527px" aria-label="Social profile one"></a>
  <a class="social" style="left:580px" aria-label="Social profile two"></a>
  <a class="social" style="left:632px" aria-label="Social profile three"></a>
</footer>
<div class="legal-bar"><span class="copy">© Copyright 2019 Harlow Stonefield</span><span class="links">Privacy Policy &nbsp;|&nbsp; Site map</span></div>

</body>
</html>
```